Velantor corporate website

Dear graphic designers,
We would like to create a brand new corporate website for our company named "Velantor".
Velantor is a small Swiss premium IT company, with very prestigious clients in the Private Banking industry.
Here would be the values which could be associated to Velantor: trustworthy, serious, modern, high tech, high quality, sobriety, elegant.
Please find attached the Velantor logo in SVG format.
Our new website will have for only purpose to present briefly the company in one page: the team of experts (4 employees), the mission, the expertise and the contact info.
Very short and concise, easy to read.
Like this website for example but even shorter: https://www.mirdalex.example/

```html
<!DOCTYPE html>
<html lang="en">
<head>
<meta charset="utf-8">
<title>Velantor — Corporate Website</title>
<link href="https://fonts.googleapis.com/css2?family=Poppins:wght@300;400;500;600;700;800&display=swap" rel="stylesheet">
<style>
:root{
  --brand:#0c55ae;
  --brand-dark:#0a4794;
  --ink:#222;
  --muted:#888;
  --soft-bg:#f1f1f1;
  --ghost-light:#eceef2;
  --ghost-grey:#e0e4ea;
  --card-line:#b9cbe4;
  --white:#fff;
}
*{margin:0;padding:0;box-sizing:border-box}
html,body{width:1200px;height:3829px;overflow:hidden}
body{font-family:'Poppins',sans-serif;color:var(--ink);background:var(--white);position:relative}
.abs{position:absolute}
section,header,footer{position:absolute;left:0;width:1200px}

/* header */
.site-header{top:0;height:100px;background:var(--white)}
.brand-name{left:86px;top:28px;font-size:32px;font-weight:600;color:var(--brand);letter-spacing:2px}
.main-nav{right:84px;top:38px;display:flex;gap:33px;font-size:15px;color:#333}

/* hero */
.hero{top:100px;height:578px;background:linear-gradient(160deg,#3f7fd0 0%,#2c69bd 45%,#1d55a6 100%)}
.hero-photo{inset:0}
.hero-title{top:228px;width:100%;text-align:center;color:var(--white);font-size:41px;font-weight:700}
.hero-text{top:300px;left:270px;width:660px;text-align:center;color:var(--white);font-size:15.5px;line-height:26px}

/* section heading */
.ghost{font-weight:800;font-size:82px;line-height:1;letter-spacing:1px;white-space:nowrap}
.section-title{font-weight:700;font-size:30px;color:var(--brand)}

/* mission */
.mission{top:678px;height:586px;background:var(--white)}
.photo-team{left:86px;top:98px;width:394px;height:292px;border-radius:8px;background:linear-gradient(135deg,#d9d6d0,#a89a85 60%,#6e6458)}
.photo-work{left:274px;top:282px;width:269px;height:223px;border-radius:8px;border:4px solid var(--white);background:linear-gradient(135deg,#7a8fa3,#3c4b5b 60%,#a79b8f)}
.mission .ghost{left:596px;top:38px;color:var(--ghost-light)}
.mission .section-title{left:600px;top:90px}
.mission-text{left:600px;top:160px;width:490px;font-size:15px;line-height:30.8px;color:#222}
.btn{left:601px;top:425px;width:159px;height:48px;background:var(--brand);color:var(--white);font-size:15px;font-weight:500;display:flex;align-items:center;justify-content:center}

/* expertise */
.expertise{top:1264px;height:1031px;background:var(--soft-bg)}
.center-ghost{width:100%;text-align:center}
.expertise .ghost{top:62px;color:var(--ghost-grey)}
.expertise .section-title{top:118px;width:100%;text-align:center}
.service{width:327px;height:339px;background:var(--white);text-align:center}
.service .icon{position:absolute;left:119px;top:59px;width:88px;height:88px;border-radius:50%;background:var(--brand);display:flex;align-items:center;justify-content:center}
.service h3{position:absolute;top:170px;width:100%;font-size:20px;font-weight:500;color:var(--brand)}
.service p{position:absolute;top:210px;left:28px;width:271px;font-size:15px;line-height:26px;color:var(--muted)}

/* team */
.team{top:2295px;height:683px;background:var(--white)}
.team .ghost{top:82px;color:var(--ghost-light)}
.team .section-title{top:136px;width:100%;text-align:center}
.member{width:236px;height:307px;top:283px;border:1.5px solid var(--card-line);border-radius:22px;background:var(--white)}
.member .portrait{position:absolute;left:40px;top:-58px;width:155px;height:155px;border-radius:50%;background:linear-gradient(180deg,#dcdcdc,#9a9a9a 55%,#3b3b3b)}
.member h4{position:absolute;left:18px;top:118px;font-size:19.5px;font-weight:500;color:var(--brand)}
.member .role{position:absolute;left:18px;top:148px;font-size:14px;color:#444}
.member .line{position:absolute;left:18px;font-size:14.5px;color:#333;display:flex;align-items:center;gap:10px}
.member .social{position:absolute;left:20px;top:258px;width:24px;height:24px;border-radius:50%;background:var(--brand)}

/* contact */
.contact{top:2978px;height:660px;background:var(--soft-bg)}
.contact .ghost{top:72px;color:var(--ghost-grey)}
.contact .section-title{top:130px;width:100%;text-align:center}
.field{background:var(--white);font-size:15px;color:#888;padding:14px 19px}
.submit{left:322px;top:531px;width:114px;height:38px;border-radius:8px;background:var(--brand);color:var(--white);font-size:14px;display:flex;align-items:center;justify-content:center}
.contact-brand{left:690px;top:258px;font-size:58px;font-weight:600;color:var(--brand);letter-spacing:4px}
.address{left:750px;top:364px;font-size:15.5px;line-height:19px;color:#222}
.phone{left:752px;top:448px;font-size:21px;color:#222}

/* footer */
.site-footer{top:3638px;height:191px;background:var(--brand)}
.footer-nav{top:62px;width:100%;display:flex;justify-content:center;gap:26px;color:var(--white);font-size:15px}
.footer-rule{left:250px;top:112px;width:700px;height:1px;background:rgba(255,255,255,.35)}
.copyright{top:140px;width:100%;text-align:center;color:var(--white);font-size:13.5px}
</style>
</head>
<body>

<header class="site-header">
  <div class="abs brand-name">VELANTOR</div>
  <nav class="abs main-nav">
    <span>Team of Experts</span><span>Our Misson</span><span>Our Expertise</span><span>Contact Us</span>
  </nav>
</header>

<section class="hero">
  <div class="abs hero-photo" role="img" aria-label="Modern glass office building against a blue sky, tinted blue"></div>
  <h1 class="abs hero-title">WELCOME TO VELANTOR</h1>
  <p class="abs hero-text">Lorem ipsum is placeholder text commonly used in the graphic, print, and publishing industries for previewing layouts and visual mockups.</p>
</section>

<section class="mission">
  <div class="abs photo-team" role="img" aria-label="Team of colleagues gathered around a laptop"></div>
  <div class="abs photo-work" role="img" aria-label="Colleagues working at laptops in an office"></div>
  <div class="abs ghost">MISSON</div>
  <h2 class="abs section-title">OUR MISSON</h2>
  <p class="abs mission-text">Lorem ipsum dolor sit amet, consectetur adipiscing elit, sed do eiusmod tempor incididunt ut labore et dolore magna aliqua. Ut enim ad minim veniam, quis nostrud exercitation ullamco laboris nisi ut aliquip ex ea commodo consequat. Duis aute irure dolor in reprehenderit in voluptate velit esse cillum dolore eu fugiat nulla pariatur. Excepteur sint occaecat cupidatat non proident, sunt in culpa qui officia deserunt mollit anim id est laborum.</p>
  <div class="abs btn">Read More</div>
</section>

<section class="expertise">
  <div class="abs ghost center-ghost">EXPERTISE</div>
  <h2 class="abs section-title">OUR EXPERTISE</h2>

  <div class="abs service" style="left:86px;top:205px">
    <div class="icon"><svg width="46" height="46" viewBox="0 0 46 46" fill="none" stroke="#fff" stroke-width="2.4"><rect x="17" y="4" width="12" height="9"/><path d="M23 13v8M9 21h28M9 21v6M37 21v6M23 21v6"/><rect x="3" y="27" width="12" height="9"/><rect x="31" y="27" width="12" height="9"/><rect x="17" y="27" width="12" height="9"/></svg></div>
    <h3>IT Management</h3>
    <p>Lorem ipsum dolor sit amet, sit le consectetur adipiscing elit, sed do eiusmod tempor</p>
  </div>
  <div class="abs service" style="left:438px;top:205px">
    <div class="icon"><svg width="48" height="40" viewBox="0 0 48 40" fill="#fff"><path d="M12 34a9 9 0 0 1-1-18 12 12 0 0 1 23-3 10 10 0 0 1 3 21z"/><circle cx="18" cy="16" r="6" fill="#0c55ae"/><path d="M18 12v6M15 16l3 3 3-3" stroke="#fff" stroke-width="2" fill="none"/></svg></div>
    <h3>Cloud Services</h3>
    <p>Lorem ipsum dolor sit amet, sit le consectetur adipiscing elit, sed do eiusmod tempor</p>
  </div>
  <div class="abs service" style="left:787px;top:205px">
    <div class="icon"><svg width="46" height="42" viewBox="0 0 46 42" fill="none" stroke="#fff" stroke-width="3"><rect x="3" y="3" width="40" height="27" rx="2"/><path d="M23 30v7M14 38h18"/></svg></div>
    <h3>Cloud Computing</h3>
    <p>Lorem ipsum dolor sit amet, sit le consectetur adipiscing elit, sed do eiusmod tempor</p>
  </div>
  <div class="abs service" style="left:86px;top:582px">
    <div class="icon"><svg width="48" height="48" viewBox="0 0 48 48" fill="none" stroke="#fff" stroke-width="2.4"><circle cx="20" cy="20" r="15"/><path d="M5 20h30M20 5c-7 8-7 22 0 30M20 5c7 8 7 22 0 30"/><path d="M30 27v14h12v-8l-6-2v-4" fill="#fff"/></svg></div>
    <h3>Web Developments</h3>
    <p>Lorem ipsum dolor sit amet, sit le consectetur adipiscing elit, sed do eiusmod tempor</p>
  </div>
  <div class="abs service" style="left:438px;top:582px">
    <div class="icon"><svg width="40" height="46" viewBox="0 0 40 46" fill="none" stroke="#fff" stroke-width="2.6"><rect x="6" y="3" width="28" height="9"/><rect x="6" y="14" width="28" height="9"/><rect x="6" y="25" width="28" height="9"/><path d="M20 34v7M8 42h24"/></svg></div>
    <h3>IT Consultancy</h3>
    <p>Lorem ipsum dolor sit amet, sit le consectetur adipiscing elit, sed do eiusmod tempor</p>
  </div>
  <div class="abs service" style="left:787px;top:582px">
    <div class="icon"><svg width="46" height="46" viewBox="0 0 46 46" fill="none" stroke="#fff" stroke-width="2.4"><circle cx="23" cy="23" r="18" stroke-dasharray="5 3"/><circle cx="23" cy="23" r="11"/><circle cx="23" cy="23" r="5" fill="#fff"/></svg></div>
    <h3>UI Design</h3>
    <p>Lorem ipsum dolor sit amet, sit le consectetur adipiscing elit, sed do eiusmod tempor</p>
  </div>
</section>

<section class="team">
  <div class="abs ghost center-ghost">OUR TEAM</div>
  <h2 class="abs section-title">TEAM OF EXPERTS</h2>

  <div class="abs member" style="left:88px">
    <div class="portrait" role="img" aria-label="Portrait of team member in light blazer"></div>
    <h4>Suspendisse auctor</h4><div class="role">Lorem ipsum dolor sit</div>
    <div class="line" style="top:190px"><svg width="12" height="16" viewBox="0 0 12 16" fill="none" stroke="#0c55ae" stroke-width="1.6"><rect x="1" y="1" width="10" height="14" rx="2"/><path d="M5 12h2"/></svg>0123 456 789</div>
    <div class="line" style="top:216px"><svg width="12" height="10" viewBox="0 0 12 10" fill="#0c55ae"><path d="M0 0h12v10H0z"/><path d="M0 0l6 5 6-5" stroke="#fff" fill="none"/></svg>info@velantor-mail.example</div>
    <div class="social"></div>
  </div>
  <div class="abs member" style="left:352px">
    <div class="portrait" role="img" aria-label="Portrait of team member in dark suit"></div>
    <h4>Suspendisse auctor</h4><div class="role">Lorem ipsum dolor sit</div>
    <div class="line" style="top:190px"><svg width="12" height="16" viewBox="0 0 12 16" fill="none" stroke="#0c55ae" stroke-width="1.6"><rect x="1" y="1" width="10" height="14" rx="2"/><path d="M5 12h2"/></svg>0123 456 789</div>
    <div class="line" style="top:216px"><svg width="12" height="10" viewBox="0 0 12 10" fill="#0c55ae"><path d="M0 0h12v10H0z"/><path d="M0 0l6 5 6-5" stroke="#fff" fill="none"/></svg>info@velantor-mail.example</div>
    <div class="social"></div>
  </div>
  <div class="abs member" style="left:617px">
    <div class="portrait" role="img" aria-label="Portrait of team member in brown jacket"></div>
    <h4>Suspendisse auctor</h4><div class="role">Lorem ipsum dolor sit</div>
    <div class="line" style="top:190px"><svg width="12" height="16" viewBox="0 0 12 16" fill="none" stroke="#0c55ae" stroke-width="1.6"><rect x="1" y="1" width="10" height="14" rx="2"/><path d="M5 12h2"/></svg>0123 456 789</div>
    <div class="line" style="top:216px"><svg width="12" height="10" viewBox="0 0 12 10" fill="#0c55ae"><path d="M0 0h12v10H0z"/><path d="M0 0l6 5 6-5" stroke="#fff" fill="none"/></svg>info@velantor-mail.example</div>
    <div class="social"></div>
  </div>
  <div class="abs member" style="left:880px">
    <div class="portrait" role="img" aria-label="Portrait of team member in black blazer"></div>
    <h4>Suspendisse auctor</h4><div class="role">Lorem ipsum dolor sit</div>
    <div class="line" style="top:190px"><svg width="12" height="16" viewBox="0 0 12 16" fill="none" stroke="#0c55ae" stroke-width="1.6"><rect x="1" y="1" width="10" height="14" rx="2"/><path d="M5 12h2"/></svg>0123 456 789</div>
    <div class="line" style="top:216px"><svg width="12" height="10" viewBox="0 0 12 10" fill="#0c55ae"><path d="M0 0h12v10H0z"/><path d="M0 0l6 5 6-5" stroke="#fff" fill="none"/></svg>info@velantor-mail.example</div>
    <div class="social"></div>
  </div>
</section>

<section class="contact">
  <div class="abs ghost center-ghost">CONTACT</div>
  <h2 class="abs section-title">CONTACT US</h2>
  <div class="abs field" style="left:159px;top:238px;width:217px;height:46px">First Name*</div>
  <div class="abs field" style="left:390px;top:238px;width:218px;height:46px">Last Name*</div>
  <div class="abs field" style="left:159px;top:298px;width:217px;height:46px">Phone*</div>
  <div class="abs field" style="left:390px;top:298px;width:218px;height:46px">Email*</div>
  <div class="abs field" style="left:159px;top:358px;width:449px;height:149px">Message*</div>
  <div class="abs submit">SUBMIT</div>

  <div class="abs contact-brand">VELANTOR</div>
  <svg class="abs" style="left:706px;top:364px" width="26" height="34" viewBox="0 0 26 34"><path d="M13 1a12 12 0 0 0-12 12c0 9 12 20 12 20s12-11 12-20A12 12 0 0 0 13 1z" fill="#0c55ae"/><circle cx="13" cy="13" r="4.5" fill="#fff"/></svg>
  <div class="abs address">Address line here dummy<br>address line here</div>
  <svg class="abs" style="left:704px;top:449px" width="30" height="30" viewBox="0 0 30 30" fill="none" stroke="#0c55ae" stroke-width="2.6"><path d="M6 3l5 6-3 3c2 4 5 7 9 9l3-3 6 5-3 4C13 27 3 17 2 7z"/><path d="M17 3a10 10 0 0 1 10 10M17 8a5 5 0 0 1 5 5"/></svg>
  <div class="abs phone">(+0123) 1234567890</div>
</section>

<footer class="site-footer">
  <nav class="abs footer-nav">
    <span>TEAM OF EXPERTS</span><span>|</span><span>OUR MISSON</span><span>|</span><span>OUR EXPERTISE</span><span>|</span><span>CONTACT US</span>
  </nav>
  <div class="abs footer-rule"></div>
  <div class="abs copyright">Copyright © 2023 All Rights Reserved By Velantor</div>
</footer>

</body>
</html>
```